International Bike and Bike Clothing distribution business needs business card design. Business is

We need a business card design for our Bike Brand distribution business. Want the company name on one side and rep/gm contact details on other side. Contact details would include, name, title, email, phone, postal address. Needs to be a bit edgy, dealing with a sporting/cycling community so can be casual but professional. Company name is 'Quilted Wheel Goods' and would like to see 'Quilted' in a cursive font (similar to Lundo Cycling brand) and 'Wheel Goods' to be separate or below 'Quilted' in a simple capital letter font. The inclusion of an image reflective of the nature of the business would be encouraged.

Industry/Entity Type

Business

Contact Information for Business Card

2 cards with following information;

Declan Whitby
Managing Director
E declan@quiltedwheelgoods.ae
M +971 (0) 56 482 3107
Trade Lic. No. TBA

Mireya Whitby
Account Manager
E mireya@quiltedwheelgoods.ae
P +971 (0) 56 216 9435
Trade Lic. No. TBA

Requirements
Must have
• Full company name is 'Quilted Wheel Goods'
• Would like Quilted to be separate and in a font similar to Lundo Cycling clothing, and would like Wheel Goods to be in capitals below. Would consider if an image of a push bike between the text was presented.

```html
<!DOCTYPE html>
<html lang="en">
<head>
<meta charset="utf-8">
<title>Quilted Wheel Goods – Business Cards</title>
<link rel="stylesheet" href="https://fonts.googleapis.com/css2?family=Questrial&display=swap">
<style>
  :root {
    --backdrop: #e9dcc3;
    --divider: #1c1c22;
    --navy: #17237a;
    --white: #ffffff;
    --ink: #2b2b2b;
    --black: #0b0b0b;
    --contact: #c9c9c9;
    --tag-red: #d81e3c;
    --tag-navy: #1a2678;
  }
  * { box-sizing: border-box; margin: 0; padding: 0; }
  html, body { width: 1200px; height: 1200px; overflow: hidden; }
  body {
    background: var(--backdrop);
    font-family: "Questrial", "Century Gothic", sans-serif;
    position: relative;
  }
  .card-set {
    position: absolute;
    left: 0;
    width: 1200px;
    height: 600px;
  }
  .card-set--red { top: 0; }
  .card-set--navy { top: 600px; }
  .set-divider {
    position: absolute;
    top: 594px;
    left: 0;
    width: 1200px;
    height: 12px;
    background: var(--divider);
  }
  .card {
    position: absolute;
    top: 130px;
    width: 570px;
    height: 340px;
    overflow: hidden;
    box-shadow: 0 6px 18px rgba(0, 0, 0, 0.35);
  }
  .card-front { left: 20px; }
  .card-back { left: 610px; background: var(--white); }
  .card svg.card-art { position: absolute; inset: 0; }

  .wordmark {
    position: absolute;
    color: var(--ink);
    font-weight: 400;
    text-align: center;
    line-height: 1;
  }
  .wordmark .wordmark-main { display: block; font-size: 74px; letter-spacing: 1px; }
  .wordmark .wordmark-sub { display: block; font-size: 21px; letter-spacing: 5px; margin-top: 10px; }
  .card-front .wordmark { left: 120px; top: 112px; width: 320px; }
  .card-back .wordmark { right: 30px; top: 28px; width: 260px; }
  .card-back .wordmark .wordmark-main { font-size: 62px; }
  .card-back .wordmark .wordmark-sub { font-size: 19px; }

  .name-tag {
    position: absolute;
    left: 0;
    top: 72px;
    width: 200px;
    height: 62px;
    color: var(--white);
    padding: 10px 0 0 14px;
  }
  .name-tag svg { position: absolute; inset: 0; z-index: 0; }
  .name-tag .person-name { position: relative; font-size: 21px; display: block; }
  .name-tag .person-title { position: relative; font-size: 12px; display: block; margin: 1px 0 0 28px; }

  .contact-list {
    position: absolute;
    left: 120px;
    top: 258px;
    width: 440px;
    color: var(--contact);
    font-size: 13.5px;
  }
  .contact-row { display: flex; align-items: center; gap: 28px; margin-bottom: 20px; }
  .contact-item { display: flex; align-items: center; gap: 8px; white-space: nowrap; }
  .contact-item svg { width: 16px; height: 16px; flex: none; }
</style>
</head>
<body>

<section class="card-set card-set--red">
  <article class="card card-front">
    <svg class="card-art" viewBox="0 0 570 340" width="570" height="340" aria-hidden="true">
      <rect width="570" height="340" fill="var(--navy)"/>
      <rect x="0" y="120" width="570" height="52" fill="var(--white)"/>
      <circle cx="280" cy="170" r="176" fill="none" stroke="var(--white)" stroke-width="5"/>
      <circle cx="280" cy="170" r="170" fill="var(--navy)"/>
      <circle cx="280" cy="170" r="145" fill="var(--white)"/>
    </svg>
    <div class="wordmark"><span class="wordmark-main">Quilted</span><span class="wordmark-sub">WHEEL GOODS</span></div>
  </article>

  <article class="card card-back">
    <svg class="card-art" viewBox="0 0 570 340" width="570" height="340" aria-hidden="true">
      <path d="M0 50 Q0 40 12 40 L62 40 Q82 40 92 62 L150 200 Q164 232 200 232 L570 232 L570 340 L0 340 Z" fill="var(--black)"/>
    </svg>
    <div class="name-tag">
      <svg viewBox="0 0 200 62" width="200" height="62" aria-hidden="true">
        <path d="M0 0 L182 0 Q194 0 192 12 L182 54 Q180 62 170 62 L0 62 Z" fill="var(--tag-red)"/>
      </svg>
      <span class="person-name">Tariq Noor</span>
      <span class="person-title">graphical designer</span>
    </div>
    <div class="wordmark"><span class="wordmark-main">Quilted</span><span class="wordmark-sub">WHEEL GOODS</span></div>
    <div class="contact-list">
      <div class="contact-row">
        <span class="contact-item">
          <svg viewBox="0 0 16 16" aria-hidden="true"><path d="M3 1 L6 1 L7 5 L5 6.5 Q6.5 9.5 9.5 11 L11 9 L15 10 L15 13 Q15 15 13 15 Q2 14 1 3 Q1 1 3 1 Z" fill="var(--contact)"/></svg>
          +91 987650321
        </span>
        <span class="contact-item">
          <svg viewBox="0 0 16 16" aria-hidden="true"><rect x="0.5" y="3" width="15" height="10" fill="var(--contact)"/><path d="M0.5 3 L8 9 L15.5 3" fill="none" stroke="var(--black)" stroke-width="1.2"/></svg>
          tariqnoor64@postbox.com
        </span>
      </div>
      <div class="contact-row">
        <span class="contact-item">
          <svg viewBox="0 0 16 16" aria-hidden="true"><path d="M8 15 Q2 8.5 2 6 A6 6 0 0 1 14 6 Q14 8.5 8 15 Z" fill="var(--contact)"/><circle cx="8" cy="6" r="2.2" fill="var(--black)"/></svg>
          riverside nagar , india 4830219
        </span>
      </div>
    </div>
  </article>
</section>

<div class="set-divider"></div>

<section class="card-set card-set--navy">
  <article class="card card-front">
    <svg class="card-art" viewBox="0 0 570 340" width="570" height="340" aria-hidden="true">
      <rect width="570" height="340" fill="var(--navy)"/>
      <rect x="0" y="120" width="570" height="52" fill="var(--white)"/>
      <circle cx="280" cy="170" r="176" fill="none" stroke="var(--white)" stroke-width="5"/>
      <circle cx="280" cy="170" r="170" fill="var(--navy)"/>
      <circle cx="280" cy="170" r="145" fill="var(--white)"/>
    </svg>
    <div class="wordmark"><span class="wordmark-main">Quilted</span><span class="wordmark-sub">WHEEL GOODS</span></div>
  </article>

  <article class="card card-back">
    <svg class="card-art" viewBox="0 0 570 340" width="570" height="340" aria-hidden="true">
      <path d="M0 50 Q0 40 12 40 L62 40 Q82 40 92 62 L150 200 Q164 232 200 232 L570 232 L570 340 L0 340 Z" fill="var(--black)"/>
    </svg>
    <div class="name-tag">
      <svg viewBox="0 0 200 62" width="200" height="62" aria-hidden="true">
        <path d="M0 0 L182 0 Q194 0 192 12 L182 54 Q180 62 170 62 L0 62 Z" fill="var(--tag-navy)"/>
      </svg>
      <span class="person-name">Tariq Noor</span>
      <span class="person-title">graphical designer</span>
    </div>
    <div class="wordmark"><span class="wordmark-main">Quilted</span><span class="wordmark-sub">WHEEL GOODS</span></div>
    <div class="contact-list">
      <div class="contact-row">
        <span class="contact-item">
          <svg viewBox="0 0 16 16" aria-hidden="true"><path d="M3 1 L6 1 L7 5 L5 6.5 Q6.5 9.5 9.5 11 L11 9 L15 10 L15 13 Q15 15 13 15 Q2 14 1 3 Q1 1 3 1 Z" fill="var(--contact)"/></svg>
          +91 987650321
        </span>
        <span class="contact-item">
          <svg viewBox="0 0 16 16" aria-hidden="true"><rect x="0.5" y="3" width="15" height="10" fill="var(--contact)"/><path d="M0.5 3 L8 9 L15.5 3" fill="none" stroke="var(--black)" stroke-width="1.2"/></svg>
          tariqnoor64@postbox.com
        </span>
      </div>
      <div class="contact-row">
        <span class="contact-item">
          <svg viewBox="0 0 16 16" aria-hidden="true"><path d="M8 15 Q2 8.5 2 6 A6 6 0 0 1 14 6 Q14 8.5 8 15 Z" fill="var(--contact)"/><circle cx="8" cy="6" r="2.2" fill="var(--black)"/></svg>
          riverside nagar , india 4830219
        </span>
      </div>
    </div>
  </article>
</section>

</body>
</html>
```